Business Card Design for Vintage Jazz

I am a vintage jazz band leader in New York City. My groups play the music of the 1920s, 1930s and 1940s. My website is marlowpeskin.com for more info on what I do.

I am looking for a two sided business card design that has the look and feel of a really nice business card from the 1930s. I need to convey with the design that my work has that vintage kind of class and style, but also conveys that we are fun and entertaining.

Most importantly it should make a bold staement. If Hollis Varnum had a card, what would it have looked like? I want a card that I feel confident will make an impact and will let people know that my work is te the top that NYC has to offer in vintage jazz..

Note that I have only decided to avoid the "committed payment" option as I have not used this service before. Assuming that I get quality work I will select a design from those presented.

Target Market(s)

people who want to hire my band for events, media, and new fans of the band

Industry/Entity Type

Performing Art

Contact Information for Business Card

Definitely a matte finish, possibly a sort of old style of paper with that brown tint? definitely a thick card.

Requirements
Must have
• FRONT
• My name: Marlow Peskin
• What I do: Bandleader, Guitarist, Vocalist, Songwriter
• Contact Details: marlowpeskin.com marlow@marlowpeskin.com 646-555-0187
• BACK
• My Social Media Links:
• facebook.marlowpeskin.com
• twitter, instagram, linkedin: marlowpeskin
• I'm also including a photo image I would like to use. The photo's background is not needed, and to be honest isn't really desireable. Just looking to use the image of me.
Nice to have
• I'm attaching which could be used as is, omitted from the card, or altered maybe with text going around the outside of the circle or in some other way. It may need some clean up to the edges of the lettering as we only use it for the website thumbnail.
• If there's space I'd like to include the text "join our mailing list for a free song download: freesong.marlowpeskin.com" If not perhaps just "Download a Free Song at: freesong.marlowpeskin.com - something to this end.
Should not have
• anything cartoony. Don't think retro 90s's vision of the swing era, think actual swing era!
• anything modern. Got to look old school
• Try to avoid dark backgrounds. Since we often play in bars and clubs where it is dar, a d
• avoid script fonts.

```html
<!DOCTYPE html>
<html lang="en">
<head>
<meta charset="utf-8">
<title>Marlow Peskin – Business Card</title>
<link href="https://fonts.googleapis.com/css2?family=Open+Sans:wght@400;600;700;800&display=swap" rel="stylesheet">
<style>
  :root {
    --backdrop: #3a3a3a;
    --card: #ffffff;
    --ink: #111111;
    --ink-soft: #333333;
    --teal: #5cc6b0;
    --photo-tone: #7d7d7d;
    --rule: #9a9a9a;
  }
  * { box-sizing: border-box; margin: 0; padding: 0; }
  html, body { width: 1200px; height: 900px; overflow: hidden; }
  body {
    background: var(--backdrop);
    font-family: "Open Sans", Arial, sans-serif;
    color: var(--ink);
    position: relative;
  }
  .card {
    position: absolute;
    left: 240px;
    width: 720px;
    height: 410px;
    background: var(--card);
    border-radius: 26px;
    overflow: hidden;
  }
  .card--back { top: 30px; }
  .card--front { top: 470px; }

  /* back side */
  .portrait {
    position: absolute;
    left: 125px; top: 120px;
    width: 210px; height: 210px;
    border-radius: 50%;
    background: radial-gradient(circle at 45% 55%, var(--photo-tone) 0%, #9aa9a4 35%, var(--teal) 70%);
  }
  .free-song {
    position: absolute;
    right: 66px; top: 118px;
    text-align: right;
  }
  .free-song__title { font-size: 19px; font-weight: 700; letter-spacing: 0.5px; }
  .free-song__url { font-size: 15px; color: var(--ink-soft); margin-top: 2px; }
  .social-handle {
    position: absolute;
    right: 48px; top: 214px;
    font-size: 15px; color: var(--ink-soft);
    display: flex; align-items: center; gap: 8px;
  }
  .social-handle__dot { width: 12px; height: 12px; border-radius: 50%; background: var(--ink); }
  .fan-page-link {
    position: absolute;
    left: 40px; bottom: 34px;
    font-size: 18px; color: var(--ink-soft);
    display: flex; align-items: center; gap: 10px;
  }
  .fan-page-link__dot { width: 12px; height: 12px; border-radius: 50%; background: var(--ink); }

  /* front side */
  .monogram {
    position: absolute;
    left: 90px; top: 118px;
    width: 210px; height: 210px;
    border-radius: 50%;
    background: var(--ink);
    display: flex; align-items: center; justify-content: center;
    text-align: center;
    color: var(--card);
    font-weight: 700;
    font-size: 24px;
    line-height: 1.15;
    letter-spacing: 1px;
  }
  .divider {
    position: absolute;
    left: 345px; top: 130px;
    width: 1px; height: 165px;
    background: var(--rule);
  }
  .identity {
    position: absolute;
    left: 372px; top: 128px;
  }
  .identity__name { font-size: 31px; font-weight: 800; letter-spacing: 1px; line-height: 1.05; }
  .identity__role { font-size: 16px; color: var(--ink-soft); line-height: 1.2; letter-spacing: 0.3px; }
  .contact { margin-top: 12px; font-size: 16px; line-height: 1.3; color: var(--ink-soft); }
  .contact b { color: var(--ink); font-weight: 700; }
</style>
</head>
<body>
  <section class="card card--back">
    <div class="portrait" role="img" aria-label="Cut-out photo of the bandleader tipping a boater hat, on a teal circle"></div>
    <div class="free-song">
      <p class="free-song__title">DOWNLOAD A FREE SONG AT</p>
      <p class="free-song__url">freesong.marlowpeskin.com</p>
    </div>
    <p class="social-handle"><span class="social-handle__dot"></span>marlowpeskin</p>
    <p class="fan-page-link"><span class="fan-page-link__dot"></span>fanpage.marlowpeskin.com</p>
  </section>

  <section class="card card--front">
    <div class="monogram">MARLOW<br>PESKIN</div>
    <div class="divider"></div>
    <div class="identity">
      <h1 class="identity__name">MARLOW PESKIN</h1>
      <p class="identity__role">BANDLEADER, GUITARIST<br>VOCALIST, SONGWRITER</p>
      <div class="contact">
        <p><b>P:</b> 646-555-0187</p>
        <p><b>E:</b> marlow@marlowpeskin.com</p>
        <p><b>W:</b> www.marlowpeskin.com</p>
      </div>
    </div>
  </section>
</body>
</html>
```